Coffee Package Design

We need a new package design for a coffee company. Need to be a mix between modern and classic design combined together. We are open to different ideas.
We changing our product name from Café Verlona to Café Rostelli. The picture upload
shows what the product looks like. We want something completely different. The name of the company should go on the back of the package.
Updates

Hello Everyone,

Please read description, we are going with a new name and design for the product.

Café Rostelli. Café Verlona is what we are replacing with Café Rostelli, we are looking for new

look and design, please submit new designs.

There is a change in the description. Please take out Premium coffee blend and replace with Italian Roast.                                    

Industry/Entity Type

Cafe

Requirements
Must have
• You can use up to 6 colors.
Please put these items on design: Café Rostelli (this is the product name), Regular Premium Blend Coffee, 100% Arabica,
Dumbrell & Sons (name of the company), Orvin, NM on the back of the package

The file uploaded is an example of one of our products and how the package film
is sized.

```html
<!DOCTYPE html>
<html lang="en">
<head>
<meta charset="utf-8">
<title>Café Rostelli – Italian Roast Package</title>
<link rel="stylesheet" href="https://fonts.googleapis.com/css2?family=Great+Vibes&family=Cinzel:wght@400&family=Open+Sans:wght@400&display=swap">
<style>
  :root {
    --roast-red: #7a1701;
    --espresso-black: #000000;
    --cream-white: #ffffff;
  }
  html, body {
    margin: 0;
    padding: 0;
    width: 1200px;
    height: 900px;
    overflow: hidden;
    background: var(--cream-white);
  }
  .package-film {
    display: block;
    width: 1200px;
    height: 900px;
  }
  .panel-base { fill: var(--roast-red); }
  .wave-black { fill: var(--espresso-black); stroke: var(--cream-white); stroke-width: 14; }
  .emblem-ring-outer { fill: var(--roast-red); }
  .emblem-ring-black { fill: var(--espresso-black); }
  .emblem-fill { fill: var(--cream-white); stroke: var(--roast-red); stroke-width: 2; }
  .emblem-art { fill: var(--roast-red); }
  .product-name {
    font-family: "Great Vibes", cursive;
    fill: var(--cream-white);
    font-size: 80px;
  }
  .company-line {
    font-family: "Cinzel", serif;
    fill: var(--cream-white);
    font-size: 35px;
    letter-spacing: 1px;
  }
  .roast-label {
    font-family: "Cinzel", serif;
    fill: var(--cream-white);
    font-size: 34px;
    letter-spacing: 1px;
  }
  .bean-claim {
    font-family: "Open Sans", sans-serif;
    fill: var(--cream-white);
    font-size: 44px;
  }
</style>
</head>
<body>
<svg class="package-film" viewBox="0 0 1300 1000" preserveAspectRatio="none" xmlns="http://www.w3.org/2000/svg">
  <defs>
    <clipPath id="panel-clip">
      <rect x="110" y="145" width="1090" height="693"/>
    </clipPath>
  </defs>

  <g clip-path="url(#panel-clip)">
    <rect class="panel-base" x="110" y="145" width="1090" height="693"/>
    <path class="wave-black"
      d="M118,120 L968,120 C968,330 770,420 650,525 C530,630 440,720 436,860 C430,680 320,540 240,430 C170,330 120,240 118,120 Z"/>
    <path class="wave-black"
      d="M1215,420 C1110,520 980,600 980,700 L980,860 L1215,860 Z"/>
  </g>

  <g class="emblem emblem-left">
    <circle class="emblem-ring-outer" cx="322" cy="260" r="66"/>
    <circle class="emblem-ring-black" cx="326" cy="262" r="62"/>
    <circle class="emblem-fill" cx="326" cy="262" r="50"/>
    <circle class="emblem-art" cx="326" cy="262" r="34" role="img" aria-label="Coffee cup with beans illustration"/>
  </g>

  <g class="emblem emblem-right">
    <circle class="emblem-ring-outer" cx="820" cy="242" r="66"/>
    <circle class="emblem-ring-black" cx="825" cy="242" r="62"/>
    <circle class="emblem-fill" cx="825" cy="242" r="50"/>
    <circle class="emblem-art" cx="825" cy="245" r="34" role="img" aria-label="Steaming coffee cup with beans illustration"/>
  </g>

  <text class="product-name" x="512" y="298">Café</text>
  <text class="product-name" x="540" y="398">Rostelli</text>

  <text class="company-line" transform="translate(232,492) rotate(90)">Dumbrell &amp; Sons</text>
  <text class="company-line" transform="translate(178,552) rotate(90)">Orvin, NM</text>

  <text class="roast-label" x="652" y="738">Italian Roast</text>

  <text class="bean-claim" transform="translate(1106,490) rotate(-90)">100% Arabica</text>
</svg>
</body>
</html>
```